SeniorPlum needs a new packaging

We are Coffee Roasters based in Versailles France.

We want a new design for our coffee packaging. The packaging is a basic brown paper bag. We are sticking on it a 99.1mm x 67.7mm Label.

We want a new design for the label. The label should have the following info : Name of the coffee, origin, one line of description, our website www.seniorplum.fr.

Enclosed you will find our logo, as well as a picture of our current packaging

The Design should be "simple yet sophisticate".

```html
<!DOCTYPE html>
<html lang="fr">
<head>
<meta charset="utf-8">
<title>SeniorPlum – Étiquette café</title>
<link href="https://fonts.googleapis.com/css2?family=Questrial&family=Open+Sans:ital,wght@0,400;1,400&display=swap" rel="stylesheet">
<style>
  :root {
    --ink: #1c1c1c;
    --paper: #ffffff;
    --frame: #0d0d0d;
    --roast: #4a2c10;
    --ribbon-light: #f3eee6;
    --ribbon-dark: #ddd4c6;
  }
  html, body {
    margin: 0;
    padding: 0;
    width: 1200px;
    height: 812px;
    overflow: hidden;
    background: var(--paper);
  }
  .label {
    position: relative;
    width: 1200px;
    height: 812px;
    box-sizing: border-box;
    border-style: solid;
    border-color: var(--frame);
    border-width: 16px 16px 20px 16px;
    background: var(--paper);
    color: var(--ink);
  }
  .brand-mark {
    position: absolute;
    left: 30px;
    top: 79px;
    width: 214px;
    height: 222px;
    border-radius: 50%;
    background: var(--ink);
  }
  .brand-name {
    position: absolute;
    left: 287px;
    top: 44px;
    width: 850px;
    height: 190px;
  }
  .brand-name text {
    font-family: "Questrial", sans-serif;
    font-size: 176px;
    fill: var(--ink);
  }
  .tagline {
    position: absolute;
    left: 289px;
    top: 254px;
    margin: 0;
    font-family: "Questrial", sans-serif;
    font-size: 50px;
    letter-spacing: 1px;
    line-height: 1;
  }
  .coffee-facts {
    position: absolute;
    left: 0;
    right: 0;
    top: 332px;
    margin: 0;
    padding: 0;
    list-style: none;
    text-align: center;
    font-family: "Open Sans", sans-serif;
    font-style: italic;
    font-size: 29px;
    line-height: 36.5px;
  }
  .url-ribbon {
    position: absolute;
    left: 199px;
    top: 641px;
    width: 770px;
    height: 97px;
  }
  .ribbon-art {
    position: absolute;
    inset: 0;
    border-radius: 48px;
    background: linear-gradient(180deg, var(--ribbon-light), var(--ribbon-dark));
  }
  .website {
    position: absolute;
    left: 0;
    right: 0;
    top: 24px;
    text-align: center;
    font-family: "Open Sans", sans-serif;
    font-size: 42px;
    line-height: 1.2;
    color: var(--roast);
    transform: rotate(-3deg);
  }
</style>
</head>
<body>
  <main class="label">
    <div class="brand-mark"></div>
    <svg class="brand-name" viewBox="0 0 850 190" aria-label="SeniorPlum">
      <text x="0" y="178" textLength="847" lengthAdjust="spacingAndGlyphs">SeniorPlum</text>
    </svg>
    <p class="tagline">Artisan Torréfacteur</p>

    <ul class="coffee-facts">
      <li>100% ARABICA DE PAPOUASIE NOUVELLE GUINEE</li>
      <li>Notes de dégustation : Long en bouche et équilibré, belle note de fruits rouges</li>
      <li>Origine : Nouvelle Guinée, Vallée Waghi, Plantation Koriba</li>
      <li>Teneur en caféine : 1,5%</li>
      <li>Espèce botannique : 100% Arabica de Papouasie - Variété Typica</li>
      <li>Méthode de récolte : Manuelle et sélective</li>
      <li>Torréfaction : A COEUR (|) (|) (|)</li>
    </ul>

    <div class="url-ribbon">
      <div class="ribbon-art" role="img" aria-label="Banderole ornementale gravée déroulée portant l'adresse du site"></div>
      <div class="website">www.seniorplum.fr</div>
    </div>
  </main>
</body>
</html>
```